Plumbing & Heating company

A leaflet containing -

Company name - Brackenfold Plumbing Solutions
logo
Mobile number - 07700 914226
Landline - 01632 870512
Email - Info@brackenfoldplumbing.example.co.uk
website - Brackenfold-plumbing.example.co.uk
Social media logos - pixgram, Chatterly

services we offer

- Boiler replacements (free quote)
- General plumbing & heating
- Tap replacements
- 1st & 2nd
- New builds & Extensions
- Cylinder replcemets

```html
<!DOCTYPE html>
<html lang="en">
<head>
<meta charset="utf-8">
<title>Brackenfold Plumbing Solutions – Leaflet</title>
<link rel="stylesheet" href="https://fonts.googleapis.com/css2?family=Poppins:wght@400;500;600;700;800&display=swap">
<style>
  :root{
    --charcoal:#3a3a3c;
    --charcoal-deep:#2e2e30;
    --blue:#2f9be0;
    --blue-bright:#33a6ea;
    --orange:#f47a3c;
    --white:#ffffff;
    --paper:#f4f5f6;
    --ink:#2d2d2f;
    --gold:#c99a2e;
  }
  *{box-sizing:border-box;margin:0;padding:0}
  html,body{width:783px;height:1200px;overflow:hidden;background:var(--paper)}
  body{font-family:"Poppins",sans-serif;color:var(--ink)}
  .leaflet{position:relative;width:783px;height:1200px;overflow:hidden;background:var(--paper)}

  /* header */
  .header{position:absolute;left:0;top:0;width:783px;height:421px;background:var(--charcoal)}
  .brand{position:absolute;left:36px;top:70px;display:flex;align-items:center;gap:10px}
  .brand-dot{width:30px;height:30px;border-radius:50%;background:var(--orange)}
  .brand-name{font-weight:700;font-size:17px;line-height:1.15;color:var(--orange);text-transform:uppercase;letter-spacing:.5px;width:220px}
  .lead{position:absolute;left:36px;top:180px;font-size:21px;font-weight:400;color:var(--white)}
  .headline{position:absolute;left:34px;top:206px;font-size:56px;font-weight:800;line-height:55px;color:var(--blue-bright);text-transform:uppercase}

  .hero-ring{position:absolute;left:358px;top:-60px;width:480px;height:480px;border-radius:50%;background:var(--orange)}
  .hero-photo{position:absolute;left:371px;top:-47px;width:454px;height:454px;border-radius:50%;
    background:radial-gradient(circle at 45% 40%,#5f86b8 0%,#3a5f92 45%,#2b3f5e 75%,#c8692f 100%)}

  /* photo strip */
  .strip-line{position:absolute;left:0;top:417px;width:502px;height:9px;background:var(--blue)}
  .strip-photo{position:absolute;top:433px;height:185px}
  .strip-photo.one{left:0;width:300px;clip-path:polygon(0 0,100% 0,88% 100%,0 100%);background:linear-gradient(120deg,#b99270,#e8e4df 60%,#c7854e)}
  .strip-photo.two{left:266px;width:150px;clip-path:polygon(22% 0,100% 0,78% 100%,0 100%);background:linear-gradient(160deg,#a87a4f,#e7e7e7 55%,#8e6a49)}
  .strip-photo.three{left:400px;width:160px;clip-path:polygon(20% 0,100% 0,100% 100%,0 100%);background:linear-gradient(150deg,#e6e1dc,#c8804b 55%,#dcd6d0)}

  /* emergency badge */
  .emergency{position:absolute;left:498px;top:356px;width:256px;height:256px;border-radius:50%;background:var(--orange)}
  .emergency-inner{position:absolute;left:13px;top:13px;width:230px;height:230px;border-radius:50%;background:var(--charcoal);overflow:hidden;text-align:center}
  .emergency-hours{margin-top:40px;font-size:66px;font-weight:600;color:var(--white);line-height:1}
  .emergency-band{position:absolute;left:0;top:120px;width:100%;height:72px;background:var(--blue);color:var(--white);text-transform:uppercase;font-weight:700;line-height:1}
  .emergency-band span{display:block}
  .emergency-band .small{font-size:26px;margin-top:6px}
  .emergency-band .big{font-size:32px;margin-top:2px}

  /* services */
  .services-title{position:absolute;left:0;top:650px;width:378px;height:50px;background:var(--orange);border-radius:0 25px 25px 0;color:var(--white);font-weight:600;font-size:28px;line-height:50px;padding-left:46px;text-transform:uppercase}
  .services-list{position:absolute;left:44px;top:724px;list-style:none;width:420px}
  .services-list li{display:flex;align-items:flex-start;gap:17px;font-weight:600;font-size:22px;line-height:38px;text-transform:uppercase;color:var(--ink)}
  .services-list li > span{width:360px}
  .services-list .note{color:var(--orange)}
  .service-icon{flex:none;width:26px;height:26px;margin-top:6px}

  /* about panel */
  .about{position:absolute;left:489px;top:618px;width:282px;height:307px;background:var(--blue);border-radius:0 0 14px 14px;color:var(--white);padding:102px 14px 0 14px;font-size:11.6px;line-height:1.36}
  .about p+p{margin-top:12px}
  .register{position:absolute;left:40px;top:40px;display:flex;align-items:center;background:var(--orange);border-radius:16px;padding:2px 12px 2px 8px;gap:6px}
  .register-label{font-size:6.5px;line-height:1.1;text-align:right;font-weight:600;width:66px}
  .register-number{font-size:22px;font-weight:600}

  .cert{position:absolute;top:959px;height:58px;border-radius:3px}
  .cert.gas{left:508px;width:118px;background:linear-gradient(90deg,var(--charcoal-deep) 58%,#f2d21b 58%)}
  .cert.boiler{left:640px;width:79px;border:2px solid #3d8a5a;background:var(--white)}

  /* contact */
  .cta{position:absolute;left:0;top:1041px;width:783px;height:40px;background:var(--orange);color:var(--white);font-weight:600;font-size:20px;line-height:40px;padding-left:38px;text-transform:uppercase}
  .footer{position:absolute;left:0;top:1081px;width:783px;height:119px;background:var(--charcoal)}
  .phone-icon{position:absolute;left:36px;top:30px;width:50px;height:56px}
  .contact{position:absolute;top:18px;color:var(--white)}
  .contact.mobile{left:96px;width:250px}
  .contact.landline{left:372px;width:262px}
  .contact-number{font-size:27px;font-weight:700;color:var(--blue-bright);line-height:1.15}
  .contact-line{font-size:11px;line-height:1.5;white-space:nowrap}
  .contact-hours{font-size:10.5px;font-weight:500;margin-top:2px}
  .divider{position:absolute;left:352px;top:28px;width:2px;height:62px;background:var(--blue)}
  .social{display:flex;align-items:center;gap:5px;font-size:10.5px;line-height:1.6;white-space:nowrap;margin-top:1px}
  .social-dot{width:10px;height:10px;border-radius:2px;background:var(--orange);flex:none}
  .social-dot.alt{background:var(--blue)}
  .seal{position:absolute;left:654px;top:-26px;width:112px;height:112px;border-radius:50%;background:radial-gradient(circle,#f3d27a 0%,var(--gold) 55%,#8a6516 100%)}
</style>
</head>
<body>
<main class="leaflet">

  <section class="header">
    <div class="hero-ring"></div>
    <div class="hero-photo" role="img" aria-label="Plumber in a blue work shirt carrying coiled red and blue hoses and an orange tool bag"></div>

    <div class="brand">
      <span class="brand-dot"></span>
      <span class="brand-name">Brackenfold Plumbing Solutions</span>
    </div>
    <p class="lead">NEED A PROFESSIONAL</p>
    <h1 class="headline">Expert<br>Plumbing<br>Services?</h1>
  </section>

  <div class="strip-line"></div>
  <div class="strip-photo one" role="img" aria-label="Copper pipework and a hot water cylinder installation"></div>
  <div class="strip-photo two" role="img" aria-label="Wall-mounted boiler with pipework below"></div>
  <div class="strip-photo three" role="img" aria-label="Copper pipes and valves fitted to a wall"></div>

  <div class="about">
    <div class="register">
      <span class="register-label">We are registered with the SureFlame Register</span>
      <span class="register-number">5180392</span>
    </div>
    <p>Brackenfold Plumbing Solutions are a young and ambitious Plumbing &amp; Heating company with close to a decade of experience. We are specialists in System design &amp; installation – 1st &amp; 2nd fix, and have a considerable experience in both new build and refurbishment projects including domestic, commercial and listed properties.</p>
    <p>We offer a wide range of services covering Winchester and the surrounding areas.</p>
  </div>

  <div class="emergency">
    <div class="emergency-inner">
      <div class="emergency-hours">24/7</div>
      <div class="emergency-band">
        <span class="small">Emergency</span>
        <span class="big">Call Out</span>
      </div>
    </div>
  </div>

  <h2 class="services-title">Our Services</h2>
  <ul class="services-list">
    <li><svg class="service-icon" viewBox="0 0 24 24"><circle cx="12" cy="12" r="10.5" fill="none" stroke="#f47a3c" stroke-width="1.5"/><path d="M7.5 12.5l3 3 6-6.5" fill="none" stroke="#2f9be0" stroke-width="2" stroke-linecap="round" stroke-linejoin="round"/></svg><span>Boiler Replacements <span class="note">(Free Quote)</span></span></li>
    <li><svg class="service-icon" viewBox="0 0 24 24"><circle cx="12" cy="12" r="10.5" fill="none" stroke="#f47a3c" stroke-width="1.5"/><path d="M7.5 12.5l3 3 6-6.5" fill="none" stroke="#2f9be0" stroke-width="2" stroke-linecap="round" stroke-linejoin="round"/></svg><span>General Plumbing &amp; Heating</span></li>
    <li><svg class="service-icon" viewBox="0 0 24 24"><circle cx="12" cy="12" r="10.5" fill="none" stroke="#f47a3c" stroke-width="1.5"/><path d="M7.5 12.5l3 3 6-6.5" fill="none" stroke="#2f9be0" stroke-width="2" stroke-linecap="round" stroke-linejoin="round"/></svg><span>Tap Replacements</span></li>
    <li><svg class="service-icon" viewBox="0 0 24 24"><circle cx="12" cy="12" r="10.5" fill="none" stroke="#f47a3c" stroke-width="1.5"/><path d="M7.5 12.5l3 3 6-6.5" fill="none" stroke="#2f9be0" stroke-width="2" stroke-linecap="round" stroke-linejoin="round"/></svg><span>1st &amp; 2nd Fix</span></li>
    <li><svg class="service-icon" viewBox="0 0 24 24"><circle cx="12" cy="12" r="10.5" fill="none" stroke="#f47a3c" stroke-width="1.5"/><path d="M7.5 12.5l3 3 6-6.5" fill="none" stroke="#2f9be0" stroke-width="2" stroke-linecap="round" stroke-linejoin="round"/></svg><span>New Builds &amp; Extensions</span></li>
    <li><svg class="service-icon" viewBox="0 0 24 24"><circle cx="12" cy="12" r="10.5" fill="none" stroke="#f47a3c" stroke-width="1.5"/><path d="M7.5 12.5l3 3 6-6.5" fill="none" stroke="#2f9be0" stroke-width="2" stroke-linecap="round" stroke-linejoin="round"/></svg><span>Cylinder Replcemets</span></li>
  </ul>

  <div class="cert gas" role="img" aria-label="Gas safety registration badge"></div>
  <div class="cert boiler" role="img" aria-label="Approved boiler installer badge"></div>

  <div class="cta">Contact us today to get a free quote</div>

  <footer class="footer">
    <svg class="phone-icon" viewBox="0 0 50 56" aria-hidden="true">
      <rect x="18" y="2" width="24" height="42" rx="4" fill="none" stroke="#33a6ea" stroke-width="3.5"/>
      <circle cx="30" cy="38" r="2" fill="#33a6ea"/>
      <path d="M4 30c0 12 8 22 22 22h6" fill="none" stroke="#33a6ea" stroke-width="7" stroke-linecap="round"/>
    </svg>
    <div class="contact mobile">
      <div class="contact-number">07700 914226</div>
      <div class="contact-line">Info@brackenfoldplumbing.example.co.uk</div>
      <div class="contact-hours">Open Monday – Sunday 24-Hours</div>
    </div>
    <div class="divider"></div>
    <div class="contact landline">
      <div class="contact-number">01632 870512</div>
      <div class="contact-line">Brackenfold-plumbing.example.co.uk</div>
      <div class="social"><span class="social-dot"></span><span class="social-dot alt"></span><span>pixgram · Chatterly: brackenfold-plumbing</span></div>
    </div>
    <div class="seal" role="img" aria-label="Gold satisfaction guarantee seal"></div>
  </footer>

</main>
</body>
</html>
```